Eye Grabbing - Travel Consultant Business Card

I need a business card that stands out. Vertical instead of horizontal, rounded edges, would love to use the same layout item for magnets. I have uploaded my current logo and tag line. Would love a cool eye-grabbing image for the front side. Can be something different than what you see on my website as I am looking to rebrand as a Leisure, Luxury & Adventure Specialist.

Target Market(s)

Leisure and Luxury Travel

Industry/Entity Type

Travel Agent

Contact Information for Business Card

Company Name - Ombrella Voyages; Name - Priya Halworth; Title - Travel Consultant; Website - www.ombrellavoyages.com ; Phone: 318-662-0954 Email priya@ombrellavoyages.com and my facebook, twitter, and Instagram handles

Font styles to use
Serif

Colors

Designer to choose colors to be used in the design.

Requirements
Must have
• my tag line of -- Dream Explore Discover
Nice to have

```html
<!DOCTYPE html>
<html lang="en">
<head>
<meta charset="utf-8">
<title>Ombrella Voyages – Business Card</title>
<link href="https://fonts.googleapis.com/css2?family=Lato:wght@400;700;900&display=swap" rel="stylesheet">
<style>
  :root {
    --page: #ffffff;
    --card-black: #1f1f20;
    --rule: #6b6b6b;
    --text-light: #f2f2f2;
    --mark-teal: #5cc9c9;
    --name-yellow: #e6e21a;
    --name-green: #3fb54a;
    --name-blue: #3a4fa8;
    --tag-yellow: #d9d52a;
    --sky-top: #1d3a4f;
    --sky-mid: #3e6478;
    --horizon: #c78a6a;
    --water: #1a2c37;
    --water-deep: #0c151b;
    --icon-blue: #1d9bd8;
    --icon-navy: #3b5998;
    --icon-pink: #d6357a;
  }
  * { box-sizing: border-box; margin: 0; padding: 0; }
  html, body { width: 1200px; height: 900px; overflow: hidden; background: var(--page); }
  body { position: relative; font-family: "Lato", sans-serif; }

  .card {
    position: absolute;
    top: 180px;
    width: 330px;
    height: 540px;
    border-radius: 26px;
    overflow: hidden;
    box-shadow: 0 6px 18px rgba(0,0,0,0.25);
  }
  .card--contact { left: 250px; background: var(--card-black); color: var(--text-light); text-align: center; }
  .card--cover { left: 620px; }

  .brand { display: flex; flex-direction: column; align-items: center; }
  .brand__mark {
    width: 66px; height: 66px; border-radius: 50%;
    background: var(--mark-teal);
  }
  .brand__name {
    margin-top: 14px;
    font-family: "Lato", sans-serif;
    font-weight: 700;
    font-size: 28px;
    letter-spacing: 0.5px;
    color: var(--text-light);
    white-space: nowrap;
  }

  .card--contact .brand { margin-top: 70px; }

  .rule { width: 240px; height: 1px; background: var(--rule); margin: 0 auto; }
  .rule--top { margin-top: 22px; }

  .person { padding: 20px 0 22px; }
  .person__name {
    font-weight: 900; font-size: 22px; letter-spacing: 0.5px; text-transform: uppercase;
    background: linear-gradient(90deg, var(--name-yellow), var(--name-green) 55%, var(--name-blue));
    -webkit-background-clip: text; background-clip: text; color: transparent;
  }
  .person__title { font-size: 14px; margin-top: 4px; }

  .contact { list-style: none; padding: 22px 0 14px; font-size: 14px; line-height: 1.55; }

  .social { display: flex; justify-content: center; gap: 6px; }
  .social__dot { width: 22px; height: 22px; border-radius: 4px; }
  .social__dot--a { background: var(--icon-blue); }
  .social__dot--b { background: var(--icon-navy); }
  .social__dot--c { background: var(--icon-pink); }
  .card--contact .social { margin-bottom: 16px; }

  .cover__photo {
    position: absolute; inset: 0;
    background:
      linear-gradient(180deg,
        var(--sky-top) 0%, var(--sky-mid) 30%, #6f8c99 42%,
        var(--horizon) 47%, #355566 50%, var(--water) 65%, var(--water-deep) 100%);
  }
  .cover__content {
    position: absolute; left: 0; right: 0; top: 320px;
    text-align: center;
  }
  .cover__content .brand__mark { width: 52px; height: 52px; }
  .cover__content .brand__name { font-size: 24px; margin-top: 10px; }
  .tagline {
    margin-top: 8px;
    font-family: "Lato", sans-serif; font-weight: 700;
    font-size: 13px; letter-spacing: 3px;
    color: var(--tag-yellow);
  }
  .card--cover .social { margin-top: 12px; }
</style>
</head>
<body>

  <section class="card card--contact" aria-label="Business card, contact side">
    <div class="brand">
      <span class="brand__mark"></span>
      <span class="brand__name">Ombrella Voyages</span>
    </div>
    <div class="rule rule--top"></div>
    <div class="person">
      <p class="person__name">Priya Halworth</p>
      <p class="person__title">Travel Consultant</p>
    </div>
    <div class="rule"></div>
    <ul class="contact">
      <li>Phone: 318-662-0954</li>
      <li>Email: priya@ombrellavoyages.com</li>
      <li>Web: www.ombrellavoyages.com</li>
    </ul>
    <div class="social" aria-label="Social media">
      <span class="social__dot social__dot--a"></span>
      <span class="social__dot social__dot--b"></span>
      <span class="social__dot social__dot--c"></span>
    </div>
    <div class="rule"></div>
  </section>

  <section class="card card--cover" aria-label="Business card, cover side">
    <div class="cover__photo" role="img" aria-label="Photograph of a calm sea at dusk under a blue cloudy sky, a distant boat on the reflective water"></div>
    <div class="cover__content">
      <div class="brand">
        <span class="brand__mark"></span>
        <span class="brand__name">Ombrella Voyages</span>
      </div>
      <p class="tagline">Dream. Explore. Discover</p>
      <div class="social" aria-label="Social media">
        <span class="social__dot social__dot--a"></span>
        <span class="social__dot social__dot--b"></span>
        <span class="social__dot social__dot--c"></span>
      </div>
    </div>
  </section>

</body>
</html>
```